VELK Website Redesign in Wix

Task:
Create a new design for all pages of the VELK technology website in Wix. Specifications are:
Color palette preferences: black, white, gray, purple, blue. See VELK Ref Doc provided.
Please refer to the VELK_ref doc for a sample of the desired color palette
Typesetting must be in Montserrat
Brand will be that of a Marketing Technology company
Looking for vibrant, highly engaging images and organized, digestible flow. Open to suggestions
Required format is Wix.
VELK logo does NOT need to be redesigned. Please use the files provided for the VELK logo.
Look and feel
Each slider illustrates characteristics of the customer's brand and the style your logo design should communicate.

```html
<!DOCTYPE html>
<html lang="en">
<head>
<meta charset="utf-8">
<title>VELK Technologies</title>
<link rel="stylesheet" href="https://fonts.googleapis.com/css2?family=Montserrat:wght@400;500;600;700;800&family=Libre+Franklin:wght@400;500&display=swap">
<style>
:root{
  --purple:#5d00e6;
  --ink:#111111;
  --text:#2a2a2a;
  --white:#ffffff;
  --card:#f7f8fb;
  --footer:#dcedf2;
  --accent:#2bb6c8;
}
*{box-sizing:border-box;margin:0;padding:0}
html,body{width:1200px;height:2516px;overflow:hidden;background:var(--white)}
body{position:relative;font-family:"Libre Franklin",sans-serif;color:var(--text)}
.nav{position:absolute;left:0;top:0;width:1200px;height:64px;background:var(--purple);display:flex;align-items:center}
.nav-brand{position:absolute;left:112px;top:14px;font-family:"Montserrat",sans-serif;font-weight:500;font-size:34px;letter-spacing:9px;color:var(--white)}
.nav-links{position:absolute;left:409px;top:23px;display:flex;gap:19px;font-size:16px;color:var(--white)}
.nav-login{position:absolute;left:1005px;top:21px;display:flex;align-items:center;gap:8px;font-family:"Montserrat",sans-serif;font-weight:700;font-size:16px;color:var(--white)}
.hero{position:absolute;left:0;top:64px;width:1200px;height:643px;background:linear-gradient(100deg,#6a6fa8 0%,#9aa3c8 35%,#b8c1d8 55%,#7f8ab8 80%,#4f5a98 100%)}
.hero-title{position:absolute;left:113px;top:225px;font-family:"Montserrat",sans-serif;font-weight:700;font-size:41px;line-height:53px;color:var(--white)}
.hero-sub{position:absolute;left:112px;top:360px;width:320px;font-size:15px;line-height:26px;color:var(--white)}
.hero-btn{position:absolute;left:111px;top:454px;width:130px;height:42px;background:var(--white);font-family:"Montserrat",sans-serif;font-weight:600;font-size:15px;color:var(--ink);display:flex;align-items:center;justify-content:center}
.section-title{position:absolute;left:0;top:785px;width:1200px;text-align:center;font-family:"Montserrat",sans-serif;font-weight:800;font-size:30px;letter-spacing:.5px;color:var(--ink)}
.milestone{position:absolute;width:300px;text-align:center}
.milestone-badge{width:110px;height:101px;margin:0 auto;background:var(--card);border-radius:6px;box-shadow:0 2px 8px rgba(0,0,0,.12);display:flex;align-items:center;justify-content:center;font-family:"Libre Franklin",sans-serif;font-size:13px;font-weight:500;color:var(--ink)}
.milestone-year{margin-top:20px;font-family:"Montserrat",sans-serif;font-weight:700;font-size:20px;color:var(--purple)}
.milestone-text{margin-top:10px;font-size:15px;line-height:23px;color:var(--text)}
.platform-photo{position:absolute;left:0;top:1500px;width:580px;height:562px;background:linear-gradient(180deg,#e8eef4 0%,#b9c4d4 40%,#5e6c86 70%,#dfe6ee 100%)}
.platform-title{position:absolute;left:652px;top:1575px;font-family:"Montserrat",sans-serif;font-weight:800;font-size:30px;line-height:39px;color:var(--ink)}
.platform-body{position:absolute;left:652px;top:1674px;width:420px;font-size:15px;line-height:28.5px;color:var(--text)}
.platform-list{position:absolute;left:652px;top:1780px;width:300px;list-style:none}
.platform-list li{position:relative;padding-left:23px;font-size:15px;line-height:23px;margin-bottom:30px}
.platform-list li::before{content:"›";position:absolute;left:0;top:-2px;color:var(--accent);font-size:19px}
.footer{position:absolute;left:0;top:2062px;width:1200px;height:454px;background:var(--footer)}
.footer-heading{position:absolute;top:82px;font-family:"Montserrat",sans-serif;font-weight:800;font-size:20px;color:var(--ink)}
.footer-links{position:absolute;left:110px;top:124px;list-style:none;font-family:"Montserrat",sans-serif;font-size:14px;line-height:29.2px;color:var(--ink)}
.footer-about{position:absolute;left:350px;top:122px;width:294px;font-family:"Montserrat",sans-serif;font-size:14.5px;line-height:25.8px;text-align:justify;color:var(--ink)}
.footer-news{position:absolute;left:737px;top:122px;width:348px;font-family:"Montserrat",sans-serif;font-size:16px;line-height:25.8px;text-align:justify;color:var(--ink)}
.news-input{position:absolute;left:736px;top:2318px;width:352px;height:41px;border:2px solid var(--ink);background:var(--footer);font-family:"Montserrat",sans-serif;font-size:15px;color:var(--ink);padding:11px 15px}
.news-btn{position:absolute;left:737px;top:2375px;width:351px;height:38px;background:var(--purple);color:var(--white);font-family:"Montserrat",sans-serif;font-weight:700;font-size:14px;display:flex;align-items:center;justify-content:center}
.socials{position:absolute;left:111px;top:2429px;display:flex;gap:17px}
.socials span{width:12px;height:12px;border-radius:50%;background:var(--ink)}
.copyright{position:absolute;left:111px;top:2451px;font-family:"Montserrat",sans-serif;font-size:16px;color:var(--ink)}
</style>
</head>
<body>
<header class="nav">
  <div class="nav-brand">VELK</div>
  <nav class="nav-links"><span>Home</span><span>How it works</span><span>VELK Applications</span><span>Company</span><span>Contact Us</span><span>More...</span></nav>
  <div class="nav-login">
    <svg width="19" height="19" viewBox="0 0 20 20"><circle cx="10" cy="10" r="9" fill="#fff"/><circle cx="10" cy="8" r="3.2" fill="#5d00e6"/><path d="M4.5 15.5c1.5-2.5 3.5-3.4 5.5-3.4s4 .9 5.5 3.4" fill="#5d00e6"/></svg>
    LOG IN
  </div>
</header>

<section class="hero" role="img" aria-label="Business team reviewing charts at a desk, overlaid with a city skyline">
</section>
<h1 class="hero-title">WELCOME TO<br>VELK Technologies</h1>
<p class="hero-sub">Increase and perfect your connection with consumers using VELK™'s patented</p>
<div class="hero-btn">Learn More</div>

<h2 class="section-title">PROVEN SUCCESS IN INNOVATION</h2>

<div class="milestone" style="left:96px;top:906px">
  <div class="milestone-badge">Corvane</div>
  <div class="milestone-year">1998</div>
  <p class="milestone-text">12 Patents NXQ:$1.566b market Cap<br>On 02/2021." patents acquired" by<br>Hillcrest software</p>
</div>
<div class="milestone" style="left:449px;top:906px">
  <div class="milestone-badge">Signal Nation</div>
  <div class="milestone-year">2001</div>
  <p class="milestone-text">7 Patents, 100 Employees, Pheonix,<br>Arizona Pionner in Internet<br>Talk Radio</p>
</div>
<div class="milestone" style="left:803px;top:906px">
  <div class="milestone-badge">Longstride</div>
  <div class="milestone-year">2003</div>
  <p class="milestone-text">120Patents,NXQ: LNGS market Cap<br>$3.15b on 4/21</p>
</div>
<div class="milestone" style="left:273px;top:1186px">
  <div class="milestone-badge">Sonivue</div>
  <div class="milestone-year">2003</div>
  <p class="milestone-text">16Patents,NXQ: LNGS market Cap<br>$258.82M on 12/20</p>
</div>
<div class="milestone" style="left:626px;top:1186px">
  <div class="milestone-badge" style="font-family:'Montserrat',sans-serif;font-size:20px;letter-spacing:5px">VELK</div>
  <div class="milestone-year">2003</div>
  <p class="milestone-text">6Patents,TargetLNGS market Cap<br>$258.82M on 12/20</p>
</div>

<div class="platform-photo" role="img" aria-label="Colleagues in suits reading documents together in a bright office"></div>
<h2 class="platform-title">OUR REVOLUTIONARY<br>PLATFORM</h2>
<p class="platform-body">Whether you're marketing software, selling a product, or looking to close a deal – find out your target market and quickly modify your campaigns to reach consumers silently</p>
<ul class="platform-list">
  <li>Our platform goes far beyond basic ad optimization to deliver individualized</li>
  <li>Content that immediately increases engagement</li>
  <li>Over any communication medium with embedded tones</li>
</ul>

<footer class="footer">
  <h3 class="footer-heading" style="left:110px">QUICK LINK</h3>
  <h3 class="footer-heading" style="left:350px">ABOUT US</h3>
  <h3 class="footer-heading" style="left:737px">NEWSLETTER</h3>
  <ul class="footer-links"><li>Home</li><li>How it works</li><li>VELK Applications</li><li>Company</li><li>Contact Us</li><li>More...</li></ul>
  <p class="footer-about">VELK™ Technology is a revolutionary platform that uses high frequency tones (known as VELK packets) imperceptible to the human ear. VELK's patented technology embeds information on an audio file for a more targeted, enhanced</p>
  <p class="footer-news">Lorem ipsum dolor sit amet, consectetur adipiscing elit, sed do eiusmod tempor incididunt ut labore et dolore magna aliqua. Ut enim ad minim veniam, quis nostrud exercitation ullamco .</p>
</footer>
<div class="news-input">Enter Email</div>
<div class="news-btn">SUBSCRIBE NOW</div>
<div class="socials"><span></span><span></span><span></span></div>
<p class="copyright">©Copyrights 2022 velktech | All Rights Reserved</p>
</body>
</html>
```